Bluewater Getaways KT needs a new Website

We have an old website that is just that - old. We need a fresh website that is professional graphic designed that has the following features.
1. Can be updated by ourselves in some areas.
2. Has a shopping cart.
3. Has links to download PDF files
4. Has links to other pages in the website
5. Includes social media links
6. Has a client log-in area
Full details in brief provided.

SORRY BUT IT'S URGENT. We've taken too long to write the details and it is now urgent. So my apologies I will be asking for designers to work quickly.

We will continue to use our existing web hosting company and url. Their is a link to the old website in the Design Brief.
Updates

UPDATE:  Please see the new file UPDATE TO DESIGN BRIEF.
Thanks for all your submissions to date.  We hope the update will assist with your designs.
As indicated in previous messages, we are happy with the Home Page + 1 Page in order to select the designer to work with in creating the full design. 

Thankyou Designers.  Much appreciate your efforts.
It's getting late here on Norfolk so I won't have much chance too review any more designs this evening.
But for your information:
Designer 7318405 Ravindra Mehta is so far the closest to what we are seeking.
Thanks again. 

Reason: Have extended to Monday 7 October to give time for designers to submit after feedback today. Especially given the time differences

Target Market(s)

Very wide audience. Current client group not that tech savvy, but we hope to broaden our market and sell more creative products, and so website needs to consider how people now use media, ie tablets & iphones.

Industry/Entity Type

Shopping

Requirements
Nice to have
• PLEASE SEE THE "UPDATE TO THE DESIGN BRIEF"

```html
<!DOCTYPE html>
<html lang="en">
<head>
<meta charset="utf-8">
<title>Bluewater Getaways KT</title>
<link rel="stylesheet" href="https://fonts.googleapis.com/css2?family=Source+Sans+3:wght@400;600&display=swap">
<style>
:root{
  --brand-orange:#f07c1c;
  --button-orange:#f5821f;
  --brand-green:#1a9b4b;
  --text:#333333;
  --text-muted:#4a4a4a;
  --band:#f3f4f3;
  --rule:#d9d9d9;
  --white:#ffffff;
}
*{margin:0;padding:0;box-sizing:border-box}
html,body{width:1004px;height:1200px;overflow:hidden}
body{position:relative;background:var(--white);font-family:"Source Sans 3",sans-serif;color:var(--text)}
.abs{position:absolute}
.top-rule{left:0;top:0;width:1004px;height:5px;background:var(--brand-green)}
.site-header{left:0;top:5px;width:1004px;height:117px;background:var(--band)}
.header-shadow{left:100px;top:122px;width:800px;height:28px;background:radial-gradient(ellipse at top,rgba(0,0,0,.08),rgba(0,0,0,0) 70%)}
.brand-name{left:73px;top:50px;font-size:26px;line-height:30px;font-weight:400;color:var(--text)}

.side-nav{left:72px;top:167px;width:207px;height:562px;background:#f2f2f2;box-shadow:0 1px 4px rgba(0,0,0,.25);padding:8px 20px 0 20px}
.side-nav ul{list-style:none}
.side-nav li{height:36px;line-height:36px;font-size:13.5px;color:var(--text);border-bottom:1px solid #e0e0e0;white-space:nowrap}
.side-nav li:last-child{border-bottom:none}

.h-orange{color:var(--brand-orange);font-weight:400}
.intro-title{left:306px;top:168px;font-size:15px;line-height:24px}
.intro-title strong{font-size:17.5px;font-weight:400}
.intro-sub{left:306px;top:196px;font-size:13px;line-height:18px}
.media{background:linear-gradient(180deg,#4d86c8 0%,#8fb8de 45%,#c8b48c 75%,#a58c66 100%)}
.slider{left:307px;top:227px;width:377px;height:230px}
.slider-caption{left:0;bottom:0;width:100%;height:34px;background:rgba(40,40,40,.6);color:var(--white);font-size:17px;line-height:34px;padding-left:12px}
.slider-arrow{top:93px;width:32px;height:32px}
.section-title{font-size:17px;line-height:24px}
.supported-title{left:306px;top:472px}
.feature{top:514px;width:140px;text-align:center}
.feature svg{display:block;margin:0 auto}
.feature h3{font-size:17px;font-weight:400;color:var(--brand-green);line-height:22px;margin-top:5px}
.feature p{font-size:12.5px;line-height:18px;color:var(--text);margin-top:4px}
.inclusive-title{left:306px;top:656px;width:380px;font-size:16px;line-height:24px}
.conditions{left:307px;top:707px;width:385px;font-size:11.5px;line-height:24px;color:var(--text-muted)}
.event-photo{left:307px;top:767px;width:377px;height:210px;background:linear-gradient(160deg,#3a2a22 0%,#8c6c58 40%,#d8d2cc 70%,#4a3a30 100%)}
.body-copy{left:307px;top:988px;width:380px;font-size:11.5px;line-height:21px;color:var(--text-muted)}

.side-title{font-size:17px;line-height:24px}
.contact-list{font-size:11.5px;line-height:21px;color:var(--text-muted)}
.rule{height:1px;background:var(--rule)}
.video{left:712px;top:593px;width:215px;height:160px;background:linear-gradient(180deg,#6a7a6a 0%,#8e9c84 45%,#6f8d4c 75%,#567a38 100%)}
.video svg{position:absolute;left:96px;top:53px}
.btn{background:var(--button-orange);color:var(--white);font-size:12.5px;text-align:center;text-transform:uppercase;font-weight:600}
.support-photo{left:712px;top:873px;width:215px;height:142px;background:linear-gradient(120deg,#c9d6e6 0%,#eef1f4 45%,#e8d8cc 70%,#f7f7f7 100%)}

.site-footer{left:0;top:1100px;width:1004px;height:100px;background:var(--band)}
.footer-links{left:73px;top:1124px;font-size:11px;line-height:16px;text-transform:uppercase;color:var(--text)}
.copyright{left:73px;top:1152px;font-size:11px;line-height:16px;color:var(--text)}
.social{top:1127px;width:30px;height:30px;background:#9aa0a6}
</style>
</head>
<body>
<div class="abs top-rule"></div>
<header class="abs site-header"></header>
<div class="abs brand-name">Bluewater Getaways KT</div>
<div class="abs header-shadow"></div>

<nav class="abs side-nav">
  <ul>
    <li>Home</li>
    <li>Governance</li>
    <li>Kelton Isle</li>
    <li>Our Mission &amp; Values</li>
    <li>Services</li>
    <li>Our Facilitators</li>
    <li>Our Shop</li>
    <li>Holiday Programs</li>
    <li>Design your own</li>
    <li>Kelton Isle Holiday</li>
    <li>OAP Creative Projects</li>
    <li>Schoolies, Siblings &amp; Family</li>
    <li>Holidays</li>
    <li>Make a Booking</li>
    <li>Testimonials</li>
  </ul>
</nav>

<main>
  <h1 class="abs intro-title h-orange">Our <strong>SOCIAL ENTERPRISE</strong> established July 2001</h1>
  <p class="abs intro-sub">Promotes</p>

  <div class="abs slider media" role="img" aria-label="Holiday group riding camels along a beach">
    <svg class="abs slider-arrow" style="left:8px" width="32" height="32" viewBox="0 0 32 32"><circle cx="16" cy="16" r="14.5" fill="rgba(255,255,255,.15)" stroke="#fff" stroke-width="2"/><path d="M18 9l-7 7 7 7" fill="none" stroke="#fff" stroke-width="2.5"/></svg>
    <svg class="abs slider-arrow" style="left:335px" width="32" height="32" viewBox="0 0 32 32"><circle cx="16" cy="16" r="14.5" fill="rgba(255,255,255,.15)" stroke="#fff" stroke-width="2"/><path d="M14 9l7 7-7 7" fill="none" stroke="#fff" stroke-width="2.5"/></svg>
    <div class="abs slider-caption">Diversity</div>
  </div>

  <h2 class="abs section-title h-orange supported-title">Supported Holidays</h2>

  <div class="abs feature" style="left:290px">
    <svg width="48" height="42" viewBox="0 0 48 42"><path d="M24 2L46 13 24 24 2 13z" fill="var(--brand-green)"/><path d="M2 21l22 11 22-11M2 28l22 11 22-11" fill="none" stroke="var(--brand-green)" stroke-width="3"/></svg>
    <h3>Travel</h3>
    <p>Lorem ipsium dolor<br>sit Pelleintes quiein<br>Nam sed metusin</p>
  </div>
  <div class="abs feature" style="left:420px">
    <svg width="42" height="42" viewBox="0 0 42 42"><path d="M21 1L40 10 21 19 2 10z" fill="var(--brand-green)"/><path d="M2 13l17 8.5V41L2 32z M40 13L23 21.5V41L40 32z" fill="var(--brand-green)"/></svg>
    <h3>Recreation</h3>
    <p>Lorem ipsium dolor<br>sit Pelleintes quiein<br>Nam sed metusin</p>
  </div>
  <div class="abs feature" style="left:553px">
    <svg width="44" height="42" viewBox="0 0 44 44"><g fill="var(--brand-green)"><rect x="18" y="1" width="8" height="42" rx="1"/><rect x="18" y="1" width="8" height="42" rx="1" transform="rotate(45 22 22)"/><rect x="18" y="1" width="8" height="42" rx="1" transform="rotate(90 22 22)"/><rect x="18" y="1" width="8" height="42" rx="1" transform="rotate(135 22 22)"/><circle cx="22" cy="22" r="15"/></g><circle cx="22" cy="22" r="6" fill="#fff"/></svg>
    <h3>Respite</h3>
    <p>Lorem ipsium dolor<br>sit Pelleintes quiein<br>Nam sed metusin</p>
  </div>

  <h2 class="abs inclusive-title h-orange">For people requiring support to participate in socially inclusive events.</h2>
  <p class="abs conditions">Intellectual Disability / Acquired Brain Injury / Mental Health / Sensory Impair ment / Frail Aged / Mobility Challenged / Siblings of children with Disabilities</p>

  <div class="abs event-photo" role="img" aria-label="Guests in matching shirts singing together at an indoor event"></div>

  <p class="abs body-copy">Nam sed metus velit, vel faucibus odio. Nullam a urna at lectus aliquetd.&nbsp; est vestibulum vestibulum odio ut congue. Cras amet dui eu purus interdum oll is sit amt sed nunc.&nbsp; Nam sed metus velit, vel faucibus odionam. Vestibiulum tortor quam, feugiat vitae, ultricies eget, tempor sit amet, ante.</p>
</main>

<aside>
  <h2 class="abs side-title h-orange" style="left:712px;top:170px">Location &amp; Contacts</h2>
  <p class="abs contact-list" style="left:712px;top:203px">Harbour Lane, Reef Point<br>PO Box 514<br>Kelton Isle NSW 2911<br>SOUTH PACIFIC<br>N.B.N. 415 672 108</p>

  <h2 class="abs side-title h-orange" style="left:712px;top:327px">Telephone</h2>
  <p class="abs contact-list" style="left:712px;top:354px">International + 67 23 51870<br>Australia 1800 419 362<br>New Zealand</p>

  <h2 class="abs side-title h-orange" style="left:712px;top:431px">Email Website &amp; FaceSpace</h2>
  <p class="abs contact-list" style="left:712px;top:459px">hello@bluewatergetaways.org<br>www.bluewatergetaways.org<br>www.facespace.com/bluewatergetaways</p>

  <div class="abs rule" style="left:712px;top:537px;width:215px"></div>

  <h2 class="abs side-title h-orange" style="left:712px;top:556px">Bluewater Hols Video</h2>
  <div class="abs video" role="img" aria-label="Video still of dancers in grass skirts performing on a lawn">
    <svg width="42" height="42" viewBox="0 0 42 42"><circle cx="21" cy="21" r="19.5" fill="#1a1a1a" stroke="#fff" stroke-width="2"/><path d="M16 12l13 9-13 9z" fill="#fff"/></svg>
  </div>

  <p class="abs contact-list" style="left:712px;top:764px;font-size:12.5px;line-height:23px;color:var(--text)">Like us on FaceSpace<br>OAP Film Festival</p>
  <div class="abs btn" style="left:832px;top:775px;width:95px;height:28px;line-height:28px">Client Login</div>

  <div class="abs rule" style="left:712px;top:825px;width:215px"></div>

  <h2 class="abs side-title h-orange" style="left:712px;top:837px">Support Us</h2>
  <div class="abs support-photo" role="img" aria-label="Support staff member wearing a headset at a help desk"></div>
  <div class="abs btn" style="left:832px;top:1033px;width:95px;height:27px;line-height:27px">Shop Now</div>
</aside>

<footer class="abs site-footer"></footer>
<p class="abs footer-links">Home | Overview | Kelton Isle | Services | Our Shop | Make a Booking | Testimonials</p>
<p class="abs copyright">Copyrights 2013. All Rights Reserved.</p>
<span class="abs social" style="left:733px" role="img" aria-label="Social link"></span>
<span class="abs social" style="left:774px" role="img" aria-label="Social link"></span>
<span class="abs social" style="left:815px" role="img" aria-label="News feed link"></span>
<span class="abs social" style="left:856px" role="img" aria-label="Video channel link"></span>
</body>
</html>
```